Vantler Helps - Pellbrook Gives Advertising Flyer

We are a vantler club that has received funding to run a community food drive project. We need a flyer for our community project that stands out . Our community project is trying to obtain non- perishable food for low income families and the vulnerable from residents in the area.
This flyer will be need to be visible and posted on store front windows and anywhere else where local residents can see it and be informed about the project. We will need a high quality version to print and a PDF version that will be e-mailed for promotional activities.

Target Market(s)

Community

Font styles to use
Sans Serif

Requirements
Must have
• My project must have logos as specified.
Nice to have
• - Images
- eye catching and modern

```html
<!DOCTYPE html>
<html lang="en">
<head>
<meta charset="utf-8">
<title>Vantler Helps – Pellbrook Gives Food Drive Flyer</title>
<link rel="stylesheet" href="https://fonts.googleapis.com/css2?family=Montserrat:wght@300;400;500;700;800;900&family=Caveat:wght@400&display=swap">
<style>
  :root {
    --brand-blue: #2460a7;
    --deep-blue: #1d4f8f;
    --brand-yellow: #f6c244;
    --white: #ffffff;
    --header-grey: #ececec;
    --bank-maroon: #8b1a3e;
  }
  html, body { margin: 0; padding: 0; overflow: hidden; background: #ffffff; }
  .flyer {
    position: relative;
    width: 849px;
    height: 1200px;
    overflow: hidden;
    font-family: "Montserrat", Arial, sans-serif;
    background: var(--brand-blue);
    color: var(--white);
  }
  .masthead {
    position: absolute; left: 0; top: 0; width: 849px; height: 193px;
    background: linear-gradient(180deg, #f7f7f7 0%, var(--header-grey) 100%);
  }
  .masthead__mark {
    position: absolute; left: 130px; top: 45px; width: 120px; height: 120px;
    border-radius: 50%; background: var(--brand-yellow);
  }
  .masthead__title {
    position: absolute; left: 282px; top: 60px; margin: 0;
    font-weight: 800; font-size: 51px; letter-spacing: 1px; line-height: 1;
    color: var(--brand-yellow);
  }
  .masthead__subtitle {
    position: absolute; left: 284px; top: 118px; margin: 0;
    font-weight: 800; font-size: 37px; letter-spacing: 0.5px; line-height: 1;
    color: var(--brand-blue);
  }
  .photo-grid { position: absolute; left: 0; top: 0; width: 849px; height: 1200px; }
  .headline {
    position: absolute; left: 37px; top: 230px; margin: 0;
    font-weight: 400; font-size: 37px; line-height: 43px;
  }
  .headline__big { display: block; font-size: 74px; line-height: 76px; font-weight: 400; letter-spacing: -1px; }
  .appeal {
    position: absolute; left: 35px; top: 538px; margin: 0;
    font-weight: 700; font-size: 45px; line-height: 1;
  }
  .appeal__name {
    position: absolute; left: 33px; top: 576px; margin: 0;
    font-weight: 900; font-size: 92px; letter-spacing: -3px; line-height: 1;
  }
  .ribbon { position: absolute; left: 76px; top: 640px; width: 420px; height: 70px; }
  .ribbon__text {
    position: absolute; left: 124px; top: 651px; margin: 0;
    font-weight: 800; font-size: 37px; line-height: 1;
    color: var(--deep-blue); transform: rotate(-2.5deg); transform-origin: left center;
  }
  .needs { position: absolute; left: 37px; top: 728px; margin: 0; padding: 0; list-style: none; }
  .needs__item {
    position: relative; padding-left: 28px; font-size: 23px; line-height: 31px;
    font-weight: 400; margin-bottom: 4px;
  }
  .needs__arrow { position: absolute; left: 0; top: 7px; width: 21px; height: 18px; }
  .mission {
    position: absolute; left: 37px; top: 881px; width: 400px; margin: 0;
    font-size: 17px; line-height: 24.5px; font-weight: 400;
  }
  .thanks {
    position: absolute; left: 32px; top: 972px; margin: 0;
    font-family: "Caveat", "Comic Sans MS", cursive;
    font-size: 62px; line-height: 1; color: var(--brand-yellow);
  }
  .supporters-label {
    position: absolute; left: 37px; top: 1080px; margin: 0;
    font-size: 19px; letter-spacing: 6px; font-weight: 400;
  }
  .supporters {
    position: absolute; left: 0; top: 1118px; width: 849px; height: 82px;
    background: var(--white);
  }
  .supporter {
    position: absolute; display: flex; align-items: center; gap: 6px;
    font-family: "Montserrat", Arial, sans-serif; font-weight: 700; font-size: 13px; line-height: 1.1;
  }
  .supporter__dot { width: 26px; height: 26px; border-radius: 50%; background: var(--brand-yellow); flex: none; }
  .supporter__square { width: 14px; height: 14px; background: var(--bank-maroon); flex: none; }
  .supporter--club { left: 40px; top: 26px; color: var(--brand-blue); }
  .supporter--council { left: 168px; top: 32px; color: #1f6e63; font-size: 14px; }
  .supporter--bank { left: 286px; top: 32px; color: var(--bank-maroon); font-size: 14px; }
  .supporter--foundation { left: 420px; top: 24px; color: var(--brand-blue); }
</style>
</head>
<body>
<div class="flyer">
  <header class="masthead">
    <div class="masthead__mark"></div>
    <h1 class="masthead__title">VANTLER HELPS</h1>
    <p class="masthead__subtitle">PELLBROOK GIVES</p>
  </header>

  <svg class="photo-grid" viewBox="0 0 849 1200" aria-hidden="false">
    <defs>
      <linearGradient id="tone-school" x1="0" y1="0" x2="0" y2="1">
        <stop offset="0" stop-color="#a9b0ae"/><stop offset="0.5" stop-color="#7d7f6b"/><stop offset="1" stop-color="#3d5a3c"/>
      </linearGradient>
      <linearGradient id="tone-volunteer" x1="0" y1="0" x2="1" y2="1">
        <stop offset="0" stop-color="#d9d6cf"/><stop offset="0.6" stop-color="#2f5fae"/><stop offset="1" stop-color="#1e3f78"/>
      </linearGradient>
      <linearGradient id="tone-bags" x1="0" y1="0" x2="1" y2="1">
        <stop offset="0" stop-color="#2b3fb0"/><stop offset="1" stop-color="#1a2a86"/>
      </linearGradient>
      <linearGradient id="tone-tree" x1="0" y1="0" x2="1" y2="0">
        <stop offset="0" stop-color="#2f4a2c"/><stop offset="0.5" stop-color="#cfc9c4"/><stop offset="1" stop-color="#6b6e77"/>
      </linearGradient>
      <linearGradient id="tone-couple" x1="0" y1="0" x2="1" y2="1">
        <stop offset="0" stop-color="#7c3a8f"/><stop offset="0.5" stop-color="#e9e1d4"/><stop offset="1" stop-color="#8c6f5c"/>
      </linearGradient>
      <linearGradient id="tone-speaker" x1="0" y1="0" x2="1" y2="1">
        <stop offset="0" stop-color="#1c1c1c"/><stop offset="0.6" stop-color="#5d5f66"/><stop offset="1" stop-color="#2a2a2a"/>
      </linearGradient>
    </defs>
    <polygon points="716,575 849,442 849,708" fill="var(--brand-yellow)"/>
    <polygon role="img" aria-label="Photo: school children in yellow caps watching a bike activity" points="709,173 851,315 709,457 567,315" fill="url(#tone-school)" stroke="var(--brand-blue)" stroke-width="6"/>
    <polygon role="img" aria-label="Photo: smiling volunteer in a blue club shirt" points="565,325 713,473 565,621 417,473" fill="url(#tone-volunteer)" stroke="var(--brand-blue)" stroke-width="6"/>
    <polygon role="img" aria-label="Photo: blue bags filled with donated groceries" points="712,585 867,740 712,895 557,740" fill="url(#tone-bags)" stroke="var(--brand-blue)" stroke-width="6"/>
    <polygon role="img" aria-label="Photo: volunteer beside a decorated tree with donated food" points="590,735 755,900 590,1065 425,900" fill="url(#tone-tree)" stroke="var(--brand-blue)" stroke-width="6"/>
    <polygon role="img" aria-label="Photo: two club members smiling at an event" points="816,865 976,1025 816,1185 656,1025" fill="url(#tone-couple)" stroke="var(--brand-blue)" stroke-width="6"/>
    <polygon role="img" aria-label="Photo: club member speaking at a lectern" points="695,990 860,1155 695,1320 530,1155" fill="url(#tone-speaker)" stroke="var(--brand-blue)" stroke-width="6"/>
  </svg>

  <h2 class="headline">Food Security and<span class="headline__big">THE COVID</span>Crisis in Pellbrook<br>YOU can make a<br>Difference</h2>

  <p class="appeal">Can you help refill</p>
  <p class="appeal__name">Dunmere's</p>
  <svg class="ribbon" viewBox="0 0 420 70" aria-hidden="true">
    <polygon points="0,21 412,2 396,28 420,52 12,68 30,44" fill="var(--brand-yellow)"/>
  </svg>
  <p class="ribbon__text">FOOD PANTRY?</p>

  <ul class="needs">
    <li class="needs__item">
      <svg class="needs__arrow" viewBox="0 0 21 18" aria-hidden="true"><path d="M1 9h16M10 2l8 7-8 7" fill="none" stroke="var(--brand-yellow)" stroke-width="3.5" stroke-linecap="round" stroke-linejoin="round"/></svg>
      We need donations of<br>non-perishable food items.
    </li>
    <li class="needs__item">
      <svg class="needs__arrow" viewBox="0 0 21 18" aria-hidden="true"><path d="M1 9h16M10 2l8 7-8 7" fill="none" stroke="var(--brand-yellow)" stroke-width="3.5" stroke-linecap="round" stroke-linejoin="round"/></svg>
      Look out for our bags and<br>information in your letter box
    </li>
  </ul>

  <p class="mission">Dunmere exists to address the immediate food insecurity of vulnerable individuals and families in the Pellbrook area.</p>

  <p class="thanks">Thank you for your support!</p>

  <p class="supporters-label">Proudly supported by:</p>

  <footer class="supporters">
    <div class="supporter supporter--club"><span>Vantler<br>Pellbrook</span><span class="supporter__dot"></span></div>
    <div class="supporter supporter--council"><span>PELLBROOK</span></div>
    <div class="supporter supporter--bank"><span class="supporter__square"></span><span>Corrin Bank</span></div>
    <div class="supporter supporter--foundation"><span>The Vantler<br>Foundation</span><span class="supporter__dot"></span></div>
  </footer>
</div>
</body>
</html>
```